8 Page Cheerleading Brochure, promoting travel options

Creation of an 8 Page A4 Brochure, portrait layout and print ready. To promote Cheerleading travel options and services to cheer gyms.
Front page to feature cheer image
Pages to include destination images and hotel images.

Colors
e34197
ec1f27

```html
<!DOCTYPE html>
<html lang="en">
<head>
<meta charset="utf-8">
<title>Cheer Travel Brochure</title>
<link rel="stylesheet" href="https://fonts.googleapis.com/css2?family=Open+Sans:wght@400;600;700;800&display=swap">
<style>
:root{
  --red:#ec1f27;
  --crimson:#b3121c;
  --wine:#870b13;
  --pink:#e34197;
  --charcoal:#262626;
  --ink:#3a3a3a;
  --grey:#e6e6e6;
  --paper:#fafafa;
  --bg:#e3e4e5;
}
*{box-sizing:border-box;margin:0;padding:0}
html,body{width:872px;height:1200px;overflow:hidden;background:var(--bg);font-family:"Open Sans",sans-serif;color:var(--ink)}
.spread{position:absolute;left:36px;width:800px;height:566px;box-shadow:0 6px 18px rgba(0,0,0,.18)}
.spread--covers{top:24px}
.spread--inside{top:610px}
.page{position:absolute;top:0;width:400px;height:566px;overflow:hidden;background:linear-gradient(180deg,var(--paper),var(--grey))}
.page--left{left:0}
.page--right{left:400px}
.layer{position:absolute;left:0;top:0}
.photo{position:absolute}
.photo--city{left:0;top:0;width:400px;height:340px;background:linear-gradient(180deg,#8ba3b8 0%,#b7c2c6 35%,#6b6a5e 62%,#3f4d4a 80%,#7a6a55 100%);clip-path:polygon(0 0,120px 0,400px 300px,400px 340px,0 340px)}
.photo--cheer{left:0;top:0;width:400px;height:390px;background:linear-gradient(180deg,#2a1416 0%,#8c1a22 30%,#c9a58e 55%,#9b2b30 75%,#d8c2b2 100%)}
.back-panel{position:absolute;right:16px;top:22px;text-align:right;color:#fff}
.back-panel .title{font-size:25px;font-weight:800;color:var(--red);letter-spacing:.5px}
.back-panel .tag{font-size:11px;margin-top:2px}
.back-panel .small{font-size:7.5px;margin-top:10px;line-height:1.45}
.back-panel .small b{font-weight:700}
.back-panel .note{font-size:7px;margin-top:8px;font-style:italic}
.contact{position:absolute;font-size:9.5px;color:var(--ink);display:flex;align-items:center;gap:4px}
.contact svg{width:11px;height:11px}
.pill{position:absolute;left:0;height:17px;padding:0 14px 0 10px;border-radius:0 9px 9px 0;background:linear-gradient(90deg,var(--wine),var(--crimson));color:#fff;font-size:8px;line-height:17px;white-space:nowrap}
.brand{position:absolute;display:flex;align-items:center;gap:5px;font-weight:800;font-size:11px;color:var(--crimson);line-height:1;letter-spacing:.3px}
.brand::before{content:"";width:12px;height:12px;border-radius:50%;background:var(--crimson)}
.cover-title{position:absolute;left:18px;top:392px;font-size:45px;font-weight:800;color:var(--red);letter-spacing:1px}
.book{position:absolute;left:276px;top:272px;width:92px;height:92px;border-radius:50%;background:var(--pink);border:4px solid #fff;box-shadow:0 2px 6px rgba(0,0,0,.3);color:#fff;font-weight:800;font-size:17px;line-height:1.05;display:flex;flex-direction:column;align-items:center;justify-content:center;text-transform:uppercase}
.about{position:absolute;left:16px;top:20px;width:368px;color:#fff}
.about h2{font-size:14px;font-weight:800;margin-bottom:8px}
.about p{font-size:7.2px;line-height:1.4;margin-bottom:9px}
.assist{position:absolute;left:16px;top:356px;width:370px;font-size:7.5px;color:var(--ink)}
.assist h3{font-size:8px;font-weight:600;margin-bottom:4px}
.assist ul{list-style:none}
.assist li{padding-left:12px;position:relative;line-height:1.55}
.assist li::before{content:"";position:absolute;left:0;top:3px;width:6px;height:6px;border-radius:50%;background:var(--pink)}
.assist p{margin-top:8px;line-height:1.4}
.services{position:absolute;left:16px;top:452px}
.services h4{font-size:7px;color:var(--crimson);font-weight:600;margin-bottom:4px}
.services ul{list-style:none;display:flex;gap:12px}
.services li{width:34px;text-align:center;font-size:5.5px;color:var(--crimson);font-weight:600}
.services .icon{display:block;width:30px;height:30px;margin:0 auto 3px;border-radius:50%;background:var(--crimson);box-shadow:inset 0 0 0 2px #fff,0 0 0 1px var(--crimson)}
.event{position:absolute;left:88px;top:20px;width:296px;color:#fff}
.event h2{font-size:11.5px;font-weight:700;margin-bottom:6px}
.event p{font-size:7px;line-height:1.4}
.price{display:inline-block;margin:14px 0 8px;background:#fff;color:var(--crimson);font-size:8px;font-weight:700;padding:2px 12px;border-radius:9px}
.event h3{font-size:7.5px;font-weight:400;margin-bottom:2px}
.event ul{list-style:none;font-size:7.5px;line-height:1.5}
.thumb{position:absolute;left:14px;width:56px;height:56px;border-radius:50%;border:3px solid #fff;box-shadow:0 1px 4px rgba(0,0,0,.35)}
.thumb--1{top:12px;background:linear-gradient(180deg,#6f8fb5,#a0543b 60%,#5d4a3a)}
.thumb--2{top:80px;background:linear-gradient(180deg,#79a6d4,#3c6b3a 65%,#8a7a62)}
.thumb--3{top:148px;background:linear-gradient(180deg,#8fb6dc,#c7b08f 50%,#3fb2c9)}
.itin{position:absolute;left:14px;top:296px;width:300px}
.itin h4{font-size:5.5px;font-weight:400;margin-bottom:4px;color:var(--ink)}
.itin table{width:372px;border-collapse:collapse;font-size:5.6px;color:var(--ink)}
.itin td{border-bottom:1px solid #fff;background:#dcdcdc;height:20px;padding:0 6px;vertical-align:middle;line-height:1.3}
.itin td:first-child{width:42px;background:#d2d2d2}
.itin td:last-child{width:72px;background:#d2d2d2}
</style>
</head>
<body>

<section class="spread spread--covers">
  <!-- back cover -->
  <article class="page page--left back-cover">
    <div class="photo photo--city" role="img" aria-label="City skyline of tall towers behind a river bridge and trees"></div>
    <svg class="layer" width="400" height="566" viewBox="0 0 400 566">
      <polygon points="120,0 400,0 400,300" fill="var(--charcoal)"/>
      <path d="M0,318 C140,372 290,356 400,296 L400,322 C290,380 140,392 0,344 Z" fill="var(--crimson)"/>
      <path d="M0,336 C140,388 290,372 400,314 L400,566 L0,566 Z" fill="var(--paper)"/>
    </svg>
    <div class="back-panel">
      <div class="title">CHEER TRAVEL</div>
      <div class="tag">Cheer Nationals, Flights &amp; Accommodation</div>
      <div class="small">Dedicated Nationals Accommodation site<br>with live rates and booking functionality<br><b>http://cheer.tripfinder.example/</b></div>
      <div class="note">Customised packages for larger groups</div>
    </div>
    <div class="contact" style="left:16px;top:470px">For more information please contact us
      <svg viewBox="0 0 12 12"><circle cx="6" cy="6" r="5.3" fill="none" stroke="var(--ink)"/><path d="M4 3.2l1 1.6-.6.7c.4.9 1 1.5 1.9 1.9l.7-.6 1.6 1-.5 1.1c-2.4-.3-4.3-2.2-4.6-4.6z" fill="var(--ink)"/></svg>
      (02) 5550 1234</div>
    <div class="pill" style="top:494px">www.northway.travel | hello@northway.travel</div>
    <div class="brand" style="left:250px;top:526px">NORTHWAY GROUP TRAVEL</div>
  </article>

  <!-- front cover -->
  <article class="page page--right front-cover">
    <div class="photo photo--cheer" role="img" aria-label="Cheerleading team in red, white and black uniforms with hair bows, seen from behind on stage"></div>
    <svg class="layer" width="400" height="566" viewBox="0 0 400 566">
      <path d="M0,330 C120,300 260,360 400,318 L400,346 C260,390 120,332 0,358 Z" fill="var(--crimson)"/>
      <path d="M0,350 C120,322 260,382 400,340 L400,566 L0,566 Z" fill="var(--paper)"/>
    </svg>
    <div class="book"><span>Book</span><span>Now</span></div>
    <div class="cover-title">CHEER TRAVEL</div>
    <div class="contact" style="left:20px;top:458px">For more information please contact us
      <svg viewBox="0 0 12 12"><circle cx="6" cy="6" r="5.3" fill="none" stroke="var(--ink)"/><path d="M4 3.2l1 1.6-.6.7c.4.9 1 1.5 1.9 1.9l.7-.6 1.6 1-.5 1.1c-2.4-.3-4.3-2.2-4.6-4.6z" fill="var(--ink)"/></svg>
      (02) 5550 1234</div>
    <div class="pill" style="top:484px">www.northway.travel | hello@northway.travel</div>
    <div class="brand" style="left:250px;top:520px">NORTHWAY GROUP TRAVEL</div>
  </article>
</section>

<section class="spread spread--inside">
  <!-- about us -->
  <article class="page page--left about-page">
    <svg class="layer" width="400" height="566" viewBox="0 0 400 566">
      <defs><linearGradient id="redTop" x1="0" y1="0" x2="1" y2="1"><stop offset="0" stop-color="var(--wine)"/><stop offset="1" stop-color="var(--crimson)"/></linearGradient></defs>
      <path d="M0,0 H400 V300 C300,330 150,300 0,334 Z" fill="url(#redTop)"/>
      <path d="M0,334 C150,300 300,330 400,300 L400,312 C300,344 150,314 0,346 Z" fill="#d9d9d9"/>
    </svg>
    <div class="about">
      <h2>ABOUT US</h2>
      <p>Northway Group Travel was established in 2001, originally specialising in Basketball Tours and quickly expanding to provide a variety of other sports options including cheerleading. Our customers have enjoyed destinations including the USA, Canada, China, Singapore, Vietnam, Europe, UK, South Africa, New Zealand and Australia.</p>
      <p>Northway are the official Travel Partner of the National All Star Cheer Federation.</p>
      <p>Our understanding of the unique requirements of group travel and our personalised approach makes us the ideal choice in planning, sourcing and managing the perfect tour for your school or club. Our ever-growing global network allows us to offer exclusive experiences that are inaccessible to others. Our dedicated Tour Coordinators thoroughly consult with teaches and coaches to tailor an itinerary and tour management plan that meets each unique set of requirements.</p>
    </div>
    <div class="assist">
      <h3>We can assist in providing:</h3>
      <ul>
        <li>Customised Itineraries</li>
        <li>Group Payment Plans</li>
        <li>Trusted, Quality Suppliers</li>
        <li>Negotiated Group Discounts on airfares, accommodation, transport and activities</li>
      </ul>
      <p>Northway's passion and mission remains to provide 'once in a lifetime' experiences to all of our valued customers.</p>
    </div>
    <div class="services">
      <h4>Services</h4>
      <ul>
        <li><span class="icon" role="img" aria-label="Rugby player icon"></span>RUGBY</li>
        <li><span class="icon" role="img" aria-label="Hockey player icon"></span>HOCKEY</li>
        <li><span class="icon" role="img" aria-label="Netball player icon"></span>NETBALL</li>
        <li><span class="icon" role="img" aria-label="Basketball player icon"></span>BASKETBALL</li>
        <li><span class="icon" role="img" aria-label="Cricket player icon"></span>CRICKET</li>
        <li><span class="icon" role="img" aria-label="Soccer player icon"></span>SOCCER</li>
        <li><span class="icon" role="img" aria-label="Volleyball player icon"></span>VOLLEYBALL</li>
      </ul>
    </div>
    <div class="pill" style="top:524px">www.northway.travel | hello@northway.travel</div>
    <div class="brand" style="left:250px;top:527px">NORTHWAY GROUP TRAVEL</div>
  </article>

  <!-- destination -->
  <article class="page page--right destination-page">
    <svg class="layer" width="400" height="566" viewBox="0 0 400 566">
      <defs><linearGradient id="redTop2" x1="0" y1="0" x2="1" y2="1"><stop offset="0" stop-color="var(--crimson)"/><stop offset="1" stop-color="var(--wine)"/></linearGradient></defs>
      <path d="M0,0 H400 V236 C300,270 150,230 0,262 Z" fill="url(#redTop2)"/>
    </svg>
    <div class="thumb thumb--1" role="img" aria-label="Hotel building exterior"></div>
    <div class="thumb thumb--2" role="img" aria-label="Palm-lined hotel driveway"></div>
    <div class="thumb thumb--3" role="img" aria-label="Resort swimming pool with mountains"></div>
    <div class="event">
      <h2>Desert Showdown. Palm Springs, California</h2>
      <p>Desert Showdown is one of the largest Cheer events in the US, run by Summit Spirit Events and is renowned for the production quality. The event is held at the Palm Springs Convention centre and draws in some of the West Coast's most talented teams. You'll see some familiar names like Golden State Flyers, Cheer Tempest, Coastline Spark, as well as many other West Coast programs.</p>
      <span class="price">Packages from $3,300</span>
      <h3>Featured accommodation</h3>
      <ul>
        <li>• Orchard Inn Anaheim</li>
        <li>• Palmview Express Cathedral City</li>
        <li>• Fairway Springs Golf Resort</li>
      </ul>
    </div>
    <div class="itin">
      <h4>Sample Itinerary</h4>
      <table>
        <tr><td>Day 1</td><td>Depart Australia. On arrival transfer to the Walk of Fame for an afternoon of sightseeing.</td><td>Los Angeles</td></tr>
        <tr><td>Day 2</td><td>Spend the day at a theme park enjoying rides, characters and shows.</td><td>Los Angeles</td></tr>
        <tr><td>Day 3</td><td>Fine tune your routine with a morning training session before transferring to Palm Springs.</td><td>Palm Springs</td></tr>
        <tr><td>Day 4</td><td>Competition Day 1</td><td>Palm Springs</td></tr>
        <tr><td>Day 5</td><td>Competition Day 2</td><td>Palm Springs</td></tr>
        <tr><td>Day 6</td><td>Ride the aerial tramway up the canyon cliffs, then an afternoon of outlet shopping.</td><td>Palm Springs</td></tr>
        <tr><td>Day 7</td><td>Transfer back to Los Angeles with time at Santa Monica before your evening flight home.</td><td>Los Angeles</td></tr>
        <tr><td>Day 8</td><td>In transit</td><td>In transit</td></tr>
        <tr><td>Day 9</td><td>Arrive home</td><td></td></tr>
      </table>
    </div>
    <div class="pill" style="top:524px">www.northway.travel | hello@northway.travel</div>
    <div class="brand" style="left:250px;top:527px">NORTHWAY GROUP TRAVEL</div>
  </article>
</section>

</body>
</html>
```